2 Professional Business Card Designs with Spot UV/ Letterhead and Email Signature

We are a high end search firm.

Vel-Or Services is a construction company.

We are looking for business cards/letterhead & email signatures that are highly professional in dark blue.

We would like front and back designs.
Updates

Thank you everyone for your submissions.  Unfortunately no one has put a watermark or shown anything with spot uv.  I am hoping for something that has depth and texture with spot uv.

Thank you again.                                    

I have attached a couple of designs as examples that show the spot uv and a watermark example.

Thanks

Target Market(s)

Management and Executives

Industry/Entity Type

Construction

Requirements
Must have
• We require a double sided card
Logo
name
Company Name
Contract, Permanent and Executive Search
Watermark of the logo (1/2moon?)
Spot UV is a must

Phone (don't care if they are icons or words or letters)
Cell
Fax
email
website
Nice to have
• linkedin address
Texture
Tagline: Bringing The Best Together

Should not have
• do not include address or
toll free #
black

```html
<!DOCTYPE html>
<html lang="en">
<head>
<meta charset="utf-8">
<title>Keystone Talent – Business Card</title>
<link rel="stylesheet" href="https://fonts.googleapis.com/css2?family=Open+Sans:wght@400;600;700&display=swap">
<style>
  :root {
    --backdrop: #e6e7ea;
    --navy: #1f4380;
    --navy-deep: #17356a;
    --navy-uv: #163366;
    --ink: #1d3c6e;
    --ink-soft: #4a5568;
    --paper: #ffffff;
    --accent: #8fa3bd;
  }
  * { margin: 0; padding: 0; box-sizing: border-box; }
  html, body { width: 1200px; height: 716px; overflow: hidden; }
  body {
    background: var(--backdrop);
    font-family: "Open Sans", Arial, sans-serif;
    position: relative;
  }
  .card {
    position: absolute;
    top: 210px;
    width: 520px;
    height: 297px;
    border-radius: 4px;
    box-shadow: 0 10px 28px rgba(0,0,0,.18);
    overflow: hidden;
  }
  .card-back {
    left: 50px;
    background: radial-gradient(circle at 50% 45%, var(--navy) 0%, var(--navy-deep) 100%);
  }
  .uv-wordmark {
    position: absolute;
    left: 0; right: 0; top: 112px;
    text-align: center;
    color: var(--navy-uv);
    font-weight: 700;
    font-size: 42px;
    letter-spacing: 1px;
    line-height: 1;
  }
  .card-front {
    left: 630px;
    background: var(--paper);
  }
  .brand {
    position: absolute;
    top: 44px;
    right: 34px;
    display: flex;
    align-items: center;
    gap: 10px;
  }
  .brand-dot {
    width: 18px; height: 18px;
    border-radius: 50%;
    background: var(--accent);
  }
  .brand-name {
    color: var(--ink);
    font-weight: 700;
    font-size: 24px;
    line-height: 1;
  }
  .contact {
    position: absolute;
    left: 30px;
    top: 120px;
    color: var(--ink-soft);
    font-size: 11.5px;
    line-height: 1.3;
  }
  .contact-name {
    color: var(--ink);
    font-size: 17px;
    letter-spacing: .5px;
    text-transform: uppercase;
    margin-bottom: 2px;
  }
  .contact-lines {
    display: grid;
    grid-template-columns: 16px auto;
    margin-top: 4px;
  }
  .contact-lines dt { color: var(--ink); }
  .website {
    position: absolute;
    right: 30px;
    bottom: 26px;
    color: var(--ink);
    font-weight: 600;
    font-size: 13px;
    letter-spacing: .3px;
  }
</style>
</head>
<body>
  <section class="card card-back" aria-label="Card back">
    <div class="uv-wordmark">Keystone Talent</div>
  </section>

  <section class="card card-front" aria-label="Card front">
    <div class="brand">
      <span class="brand-dot"></span>
      <span class="brand-name">Keystone Talent</span>
    </div>

    <div class="contact">
      <p class="contact-name">Dana Whitfield</p>
      <p>Keystone Talent Group Inc.</p>
      <p>Contract, Permanent &amp; Executive Search</p>
      <dl class="contact-lines">
        <dt>t</dt><dd>ext 214 555 0142</dd>
        <dt>m</dt><dd>555 018 3326</dd>
        <dt>f</dt><dd>555 018 3327</dd>
        <dt>e</dt><dd>dana@keystonetalent.ca</dd>
      </dl>
    </div>

    <p class="website">www.keystonetalent.ca</p>
  </section>
</body>
</html>
```